Updated website design needed for Radiology Group, Pinebrook Valley Imaging Partners

Clean, uncluttered, updated design needed for top regional Radiology Center. Focus on personal, patient oriented design, (not clinical). Should be simple and easy to navigate, with clear CTAs. Use blues, greens and photos of people in the Central Oregon outdoors.
Uncoded, PSD design only. 2 pages: Home page and one example interior page.
reference current site: http://www.pvipgroup.example/
Sites they like:
http://www.harborscanclinic.example/
http://www.mtqe.example/handler.cfm?event=practice,main
http://www.lindenbonecare.example/

Industry/Entity Type

Medical Imaging

Number of Pages Required

2 page

Font styles to use
Sans Serif

Requirements
Must have
• Personal and patient friendly.
• Lots of white space, clean and uncluttered. Clear CTAs, such as: Patient Bill Pay, Make an Appointment, Meet Our Doctors
• Use copy and contact information from the current site.
• Use outdoor images from Central Oregon, late Winter/ Spring (snow, light colors, spring green, for example)
• Include one example interior page, either Your Exam or Meet Our Doctors
Nice to have
• The client likes:
• Meet Our Doctors slider section, and big, easy to navigate Information Center on www.lindenbonecare.example
• The personal feel of the Your Exam section on www.harborscanclinic.example
• Blues and Greens, outdoorsy imagery
Should not have
• The client does not like:
• complex drop down menus
• clinical feel
• Do not use lorum ipsum or dummy text.
• Do not use outdoor images from other regions. Do not use Summer (hot, poolside) or Fall (red/orange leaves) images.

```html
<!DOCTYPE html>
<html lang="en">
<head>
<meta charset="utf-8">
<title>Meet Our Doctors – Pinebrook Valley Imaging Partners</title>
<link href="https://fonts.googleapis.com/css2?family=Roboto:wght@400;500;700&family=Oswald:wght@400;500&display=swap" rel="stylesheet">
<style>
:root{
  --blue:#1b8ac9;
  --blue-dark:#1768a2;
  --nav-top:#2b93d1;
  --nav-bottom:#1a6ba8;
  --green:#2f8a4e;
  --ink:#2b2b2b;
  --text:#444;
  --muted:#9a9a9a;
  --card:#f2f2f2;
  --line:#d8d8d8;
  --black:#111;
  --white:#fff;
}
*{box-sizing:border-box;margin:0;padding:0}
html,body{width:1200px;height:2261px;overflow:hidden;background:var(--white);font-family:'Roboto',Arial,sans-serif;color:var(--text)}
.page{position:relative;width:1200px;height:2261px}
.abs{position:absolute}
/* header */
.brand{left:89px;top:24px;display:flex;align-items:center;gap:14px}
.brand-mark{width:78px;height:78px;background:#6f79b8}
.brand-name{font-size:22px;font-weight:400;color:#333;line-height:1.15;width:170px}
.phone{left:510px;top:42px;display:flex;align-items:center;gap:12px;font-size:22px;color:#333}
.btn{top:39px;height:47px;color:var(--white);font-size:14px;font-weight:500;display:flex;align-items:center;justify-content:center;border-radius:2px;text-transform:uppercase}
.btn-pay{left:737px;width:174px;background:var(--green)}
.btn-appt{left:921px;width:191px;background:#2a2a2a}
/* nav */
.nav{left:0;top:130px;width:1200px;height:68px;background:linear-gradient(var(--nav-top),var(--nav-bottom))}
.nav a{position:absolute;top:0;height:68px;line-height:68px;color:var(--white);font-size:13.5px;text-decoration:none;text-transform:uppercase}
.nav a.active{background:#2b2b2b;padding:0 20px}
/* hero */
.hero{left:0;top:198px;width:1200px;height:200px;background:linear-gradient(90deg,#6d7478,#b9c0c3 30%,#d7dcde 55%,#9aa2a6 80%,#6b7276)}
.hero h1{position:absolute;left:0;top:0;width:100%;line-height:200px;text-align:center;font-family:'Oswald',Arial,sans-serif;font-weight:500;font-size:37px;color:var(--white)}
/* doctor cards */
.card{width:433px;height:220px;background:var(--card);border:1px solid var(--line);box-shadow:0 2px 4px rgba(0,0,0,.15)}
.portrait{position:absolute;left:-78px;top:30px;width:152px;height:152px;border-radius:50%;border:4px solid var(--white);background:radial-gradient(circle at 50% 40%,#8d949a,#4e555b);box-shadow:0 2px 6px rgba(0,0,0,.35)}
.card h2{position:absolute;left:83px;top:24px;font-size:18.5px;font-weight:400;color:var(--blue-dark)}
.card dl{position:absolute;left:88px;top:58px;font-size:10.5px;line-height:26.5px;color:var(--text)}
.card dl div{white-space:nowrap}
.card dt{display:inline;color:#222}
.card dd{display:inline}
/* partners */
.partner{top:1826px;height:38px;background:#b5b5b5;border-radius:3px}
/* footer */
.footer{left:0;top:1915px;width:1200px;height:266px;background:var(--blue)}
.fcol{position:absolute;top:40px;color:var(--white)}
.fcol h3{font-size:15px;font-weight:500;text-transform:uppercase;margin-bottom:10px}
.fcol li{list-style:none;font-size:11.5px;line-height:26px;display:flex;align-items:center;gap:7px}
.social li{line-height:43px;gap:14px;font-size:13px}
.social .ring{width:33px;height:33px;border:1.5px solid var(--white);border-radius:50%}
.bottom{left:0;top:2181px;width:1200px;height:80px;background:var(--black);color:var(--white);font-size:12px;text-align:center;line-height:80px}
</style>
</head>
<body>
<div class="page">

<header>
  <div class="abs brand"><span class="brand-mark"></span><span class="brand-name">Pinebrook Valley Imaging Partners</span></div>
  <div class="abs phone">
    <svg width="38" height="38" viewBox="0 0 38 38"><circle cx="19" cy="19" r="17.5" fill="none" stroke="#2f8a4e" stroke-width="1.5"/><path d="M13 12c1-1 2-1 3 0l2 2.5c.6.8.4 1.6-.3 2.2l-1 .8c.9 1.8 2.2 3.1 4 4l.8-1c.6-.7 1.4-.9 2.2-.3l2.5 2c1 1 1 2 0 3l-1 1c-1.5 1.5-5 .5-8.5-3s-4.5-7-3-8.5z" fill="#2f8a4e"/></svg>
    (555) 214-7080
  </div>
  <a class="abs btn btn-pay">Patient Bill Pay</a>
  <a class="abs btn btn-appt">Make an Appointment</a>
</header>

<nav class="abs nav">
  <a class="active" style="left:89px">Home</a>
  <a style="left:188px">About Us</a>
  <a style="left:294px">Our Services</a>
  <a style="left:427px">For Patients</a>
  <a style="left:559px">Our Physicians</a>
  <a style="left:707px">For Physicians</a>
  <a style="left:850px">Appointments</a>
  <a style="left:992px">Our Locations</a>
</nav>

<section class="abs hero" role="img" aria-label="Two hikers walking a snowy forest trail in winter">
  <h1>MEET OUR DOCTORS</h1>
</section>

<main>
  <article class="abs card" style="left:148px;top:507px"><div class="portrait" role="img" aria-label="Portrait of Dr. Aaron Whitcomb"></div><h2>Aaron Whitcomb, M.D.</h2><dl><div><dt>SPECIALTY</dt> : <dd>Musculoskeletal Radiology, Diagnostic Radiology</dd></div><div><dt>Certification</dt> : <dd>National Imaging Board, 2015</dd></div><div><dt>MEDICAL SCHOOL</dt> : <dd>Prairie State Medical College, 2009</dd></div><div><dt>RESIDENCY</dt> : <dd>Cascade Health University, 2014</dd></div><div><dt>FELLOWSHIP</dt> : <dd>Front Range Medical Institute, 2015</dd></div></dl></article>
  <article class="abs card" style="left:677px;top:507px"><div class="portrait" role="img" aria-label="Portrait of Dr. Marla Densford-Hale"></div><h2>Marla Densford-Hale, M.D.</h2><dl><div><dt>SPECIALTY</dt> : <dd>Musculoskeletal Radiology, Diagnostic Radiology</dd></div><div><dt>Certification</dt> : <dd>National Imaging Board, 2015</dd></div><div><dt>MEDICAL SCHOOL</dt> : <dd>Prairie State Medical College, 2009</dd></div><div><dt>RESIDENCY</dt> : <dd>Cascade Health University, 2014</dd></div><div><dt>FELLOWSHIP</dt> : <dd>Front Range Medical Institute, 2015</dd></div></dl></article>

  <article class="abs card" style="left:148px;top:751px"><div class="portrait" role="img" aria-label="Portrait of Dr. Evan Larkmoor"></div><h2>Evan Larkmoor, M.D.</h2><dl><div><dt>SPECIALTY</dt> : <dd>Musculoskeletal Radiology, Diagnostic Radiology</dd></div><div><dt>Certification</dt> : <dd>National Imaging Board, 2015</dd></div><div><dt>MEDICAL SCHOOL</dt> : <dd>Prairie State Medical College, 2009</dd></div><div><dt>RESIDENCY</dt> : <dd>Cascade Health University, 2014</dd></div><div><dt>FELLOWSHIP</dt> : <dd>Front Range Medical Institute, 2015</dd></div></dl></article>
  <article class="abs card" style="left:677px;top:751px"><div class="portrait" role="img" aria-label="Portrait of Dr. Howard T. Pell"></div><h2>Howard T. Pell, M.D.</h2><dl><div><dt>SPECIALTY</dt> : <dd>Musculoskeletal Radiology, Diagnostic Radiology</dd></div><div><dt>Certification</dt> : <dd>National Imaging Board, 2015</dd></div><div><dt>MEDICAL SCHOOL</dt> : <dd>Prairie State Medical College, 2009</dd></div><div><dt>RESIDENCY</dt> : <dd>Cascade Health University, 2014</dd></div><div><dt>FELLOWSHIP</dt> : <dd>Front Range Medical Institute, 2015</dd></div></dl></article>

  <article class="abs card" style="left:148px;top:999px"><div class="portrait" role="img" aria-label="Portrait of Dr. Daniel R. Frayne"></div><h2>Daniel R. Frayne, M.D.</h2><dl><div><dt>SPECIALTY</dt> : <dd>Musculoskeletal Radiology, Diagnostic Radiology</dd></div><div><dt>Certification</dt> : <dd>National Imaging Board, 2015</dd></div><div><dt>MEDICAL SCHOOL</dt> : <dd>Prairie State Medical College, 2009</dd></div><div><dt>RESIDENCY</dt> : <dd>Cascade Health University, 2014</dd></div><div><dt>FELLOWSHIP</dt> : <dd>Front Range Medical Institute, 2015</dd></div></dl></article>
  <article class="abs card" style="left:677px;top:999px"><div class="portrait" role="img" aria-label="Portrait of Dr. Colin Ashgrove"></div><h2>Colin Ashgrove, M.D.</h2><dl><div><dt>SPECIALTY</dt> : <dd>Musculoskeletal Radiology, Diagnostic Radiology</dd></div><div><dt>Certification</dt> : <dd>National Imaging Board, 2015</dd></div><div><dt>MEDICAL SCHOOL</dt> : <dd>Prairie State Medical College, 2009</dd></div><div><dt>RESIDENCY</dt> : <dd>Cascade Health University, 2014</dd></div><div><dt>FELLOWSHIP</dt> : <dd>Front Range Medical Institute, 2015</dd></div></dl></article>

  <article class="abs card" style="left:148px;top:1248px"><div class="portrait" role="img" aria-label="Portrait of Dr. Peter Lindqvale"></div><h2>Peter Lindqvale, M.D.</h2><dl><div><dt>SPECIALTY</dt> : <dd>Musculoskeletal Radiology, Diagnostic Radiology</dd></div><div><dt>Certification</dt> : <dd>National Imaging Board, 2015</dd></div><div><dt>MEDICAL SCHOOL</dt> : <dd>Prairie State Medical College, 2009</dd></div><div><dt>RESIDENCY</dt> : <dd>Cascade Health University, 2014</dd></div><div><dt>FELLOWSHIP</dt> : <dd>Front Range Medical Institute, 2015</dd></div></dl></article>
  <article class="abs card" style="left:677px;top:1248px"><div class="portrait" role="img" aria-label="Portrait of Dr. Russell K. Ormand"></div><h2>Russell K. Ormand, M.D.</h2><dl><div><dt>SPECIALTY</dt> : <dd>Musculoskeletal Radiology, Diagnostic Radiology</dd></div><div><dt>Certification</dt> : <dd>National Imaging Board, 2015</dd></div><div><dt>MEDICAL SCHOOL</dt> : <dd>Prairie State Medical College, 2009</dd></div><div><dt>RESIDENCY</dt> : <dd>Cascade Health University, 2014</dd></div><div><dt>FELLOWSHIP</dt> : <dd>Front Range Medical Institute, 2015</dd></div></dl></article>

  <article class="abs card" style="left:148px;top:1495px"><div class="portrait" role="img" aria-label="Portrait of Dr. Grant L. Tevison"></div><h2>Grant L. Tevison, M.D.</h2><dl><div><dt>SPECIALTY</dt> : <dd>Musculoskeletal Radiology, Diagnostic Radiology</dd></div><div><dt>Certification</dt> : <dd>National Imaging Board, 2015</dd></div><div><dt>MEDICAL SCHOOL</dt> : <dd>Prairie State Medical College, 2009</dd></div><div><dt>RESIDENCY</dt> : <dd>Cascade Health University, 2014</dd></div><div><dt>FELLOWSHIP</dt> : <dd>Front Range Medical Institute, 2015</dd></div></dl></article>
  <article class="abs card" style="left:677px;top:1495px"><div class="portrait" role="img" aria-label="Portrait of Dr. Martin A. Solvey"></div><h2>Martin A. Solvey, M.D.</h2><dl><div><dt>SPECIALTY</dt> : <dd>Musculoskeletal Radiology, Diagnostic Radiology</dd></div><div><dt>Certification</dt> : <dd>National Imaging Board, 2015</dd></div><div><dt>MEDICAL SCHOOL</dt> : <dd>Prairie State Medical College, 2009</dd></div><div><dt>RESIDENCY</dt> : <dd>Cascade Health University, 2014</dd></div><div><dt>FELLOWSHIP</dt> : <dd>Front Range Medical Institute, 2015</dd></div></dl></article>
</main>

<section aria-label="Partners">
  <div class="abs partner" style="left:129px;width:67px"></div>
  <div class="abs partner" style="left:254px;width:114px"></div>
  <div class="abs partner" style="left:430px;width:108px"></div>
  <div class="abs partner" style="left:597px;width:110px"></div>
  <div class="abs partner" style="left:794px;width:84px"></div>
  <div class="abs partner" style="left:952px;width:118px"></div>
</section>

<footer class="abs footer">
  <div class="fcol" style="left:92px"><h3>For Patients</h3><ul><li>» About Your Visit</li><li>» Why Choose Us?</li><li>» Patient Forms</li><li>» Billing and Insurance</li><li>» Locations and Maps</li><li>» Appointments</li></ul></div>
  <div class="fcol" style="left:324px"><h3>Quick Links</h3><ul><li>» Home</li><li>» About Us</li><li>» Our Physicians</li><li>» For Physicians</li><li>» Disclaimer</li><li>» HIPAA</li></ul></div>
  <div class="fcol" style="left:528px"><h3>Our Services</h3><ul><li>» Our Services</li><li>» Mammography</li><li>» MRI</li><li>» CT-64</li><li>» X-Ray</li><li>» Nuclear Medicine</li></ul></div>
  <div class="fcol" style="left:736px"><h3>Our Services</h3><ul>
    <li><svg width="10" height="10" viewBox="0 0 10 10"><path d="M1.5 1c.5-.5 1-.5 1.5 0l1 1.3c.3.4.2.8-.1 1.1l-.5.4c.5.9 1.1 1.5 2 2l.4-.5c.3-.3.7-.4 1.1-.1l1.3 1c.5.5.5 1 0 1.5l-.5.5c-.8.8-2.5.2-4.3-1.5S.2 2.8 1 2z" fill="#fff"/></svg>(555) 214-7080 - Main Line</li>
    <li><svg width="10" height="10" viewBox="0 0 10 10"><path d="M1.5 1c.5-.5 1-.5 1.5 0l1 1.3c.3.4.2.8-.1 1.1l-.5.4c.5.9 1.1 1.5 2 2l.4-.5c.3-.3.7-.4 1.1-.1l1.3 1c.5.5.5 1 0 1.5l-.5.5c-.8.8-2.5.2-4.3-1.5S.2 2.8 1 2z" fill="#fff"/></svg>(555) 214-7091 - Scheduling</li>
    <li><svg width="10" height="10" viewBox="0 0 10 10"><path d="M1.5 1c.5-.5 1-.5 1.5 0l1 1.3c.3.4.2.8-.1 1.1l-.5.4c.5.9 1.1 1.5 2 2l.4-.5c.3-.3.7-.4 1.1-.1l1.3 1c.5.5.5 1 0 1.5l-.5.5c-.8.8-2.5.2-4.3-1.5S.2 2.8 1 2z" fill="#fff"/></svg>(555) 214-7102 - Billing</li>
    <li><svg width="10" height="10" viewBox="0 0 10 10"><path d="M1.5 1c.5-.5 1-.5 1.5 0l1 1.3c.3.4.2.8-.1 1.1l-.5.4c.5.9 1.1 1.5 2 2l.4-.5c.3-.3.7-.4 1.1-.1l1.3 1c.5.5.5 1 0 1.5l-.5.5c-.8.8-2.5.2-4.3-1.5S.2 2.8 1 2z" fill="#fff"/></svg>(555) 214-7113 - Medical Records</li>
  </ul></div>
  <div class="fcol social" style="left:1008px"><h3>Follow Us On</h3><ul>
    <li><span class="ring"></span>Friendsphere</li>
    <li><span class="ring"></span>Chirpline</li>
    <li><span class="ring"></span>Photolane</li>
  </ul></div>
</footer>

<div class="abs bottom">Copyright © 2016. All Rights Reserved</div>

</div>
</body>
</html>
```